Business Card Design for TrailStocked

TrailStocked is an online e-commerce store specializing in Outdoors Gear such as camping equipment, hunting and shooting equipment, tactical gear and more. See complete line at trailstocked.org
Logo: http://www.trailstocked.org/media/ID/Stocked.jpg
http://www.trailstocked.org/media/ID/TrailStocked-blue.jpg

Target Market(s)

20-40 Male

Industry/Entity Type

E-Commerce

```html
<!DOCTYPE html>
<html lang="en">
<head>
<meta charset="utf-8">
<title>TrailStocked Business Card</title>
<link href="https://fonts.googleapis.com/css2?family=Bitter:wght@700&family=Source+Sans+3:wght@400;600;700&display=swap" rel="stylesheet">
<style>
  :root {
    --navy: #123e69;
    --navy-deep: #0f3459;
    --navy-light: #17497a;
    --navy-strip: #0c2c4d;
    --orange: #f7941d;
    --orange-red: #f15a29;
    --white: #ffffff;
    --backdrop: #e9e6e1;
  }
  * { margin: 0; padding: 0; box-sizing: border-box; }
  html, body {
    width: 1200px; height: 900px; overflow: hidden;
    background: var(--backdrop);
    font-family: "Source Sans 3", sans-serif;
  }
  .canvas { position: relative; width: 1200px; height: 900px; }
  .card {
    position: absolute; top: 296px; width: 540px; height: 308px;
    overflow: hidden; box-shadow: 0 4px 14px rgba(0,0,0,.18);
  }
  .card--front { left: 45px; }
  .card--back { left: 615px; }

  .card__brand-area {
    position: absolute; left: 0; top: 0; width: 100%; height: 127px;
    background: var(--white);
    display: flex; align-items: center; justify-content: center; gap: 12px;
  }
  .brand-square { width: 30px; height: 30px; background: var(--navy); }
  .brand-text { display: flex; flex-direction: column; }
  .brand-name {
    font-family: "Bitter", serif; font-weight: 700; font-size: 28px;
    color: var(--navy); line-height: 1;
  }
  .brand-tagline {
    font-weight: 600; font-size: 13px; color: var(--navy);
    letter-spacing: .6px; margin-top: 4px; white-space: nowrap;
  }

  .card__panel {
    position: absolute; left: 0; top: 127px; width: 100%; height: 181px;
    background: linear-gradient(90deg, var(--navy-deep), var(--navy-light));
  }
  .person { position: absolute; left: 70px; top: 51px; text-align: center; color: var(--white); }
  .person__name { font-weight: 700; font-size: 18.5px; }
  .person__role { font-size: 14px; margin-top: 1px; }

  .contact { position: absolute; left: 303px; top: 13px; color: var(--white); font-size: 14px; line-height: 18.5px; }
  .contact__address { margin-bottom: 8px; }
  .contact__line { display: flex; align-items: center; gap: 6px; }
  .contact__line svg { width: 13px; height: 13px; flex: none; }

  .card__stripe { position: absolute; left: 0; bottom: 0; width: 540px; height: 32px; }

  .card--back {
    background: linear-gradient(180deg, var(--navy-deep) 0, var(--navy-deep) 127px, var(--navy) 127px, var(--navy-light) 100%);
  }
  .back-brand {
    position: absolute; left: 120px; top: 110px; width: 120px;
    display: flex; flex-direction: column; align-items: center; gap: 8px;
  }
  .back-brand .brand-square { background: var(--white); width: 34px; height: 34px; }
  .back-brand__name { font-weight: 700; font-size: 17px; color: var(--white); }
  .back-divider {
    position: absolute; left: 250px; top: 80px; width: 1.5px; height: 130px;
    background: linear-gradient(180deg, rgba(255,255,255,0), rgba(255,255,255,.85) 30%, rgba(255,255,255,.85) 70%, rgba(255,255,255,0));
  }
  .back-tagline {
    position: absolute; left: 260px; top: 102px;
    color: var(--white); font-weight: 600; font-size: 23.5px; line-height: 31px;
  }
</style>
</head>
<body>
<main class="canvas">

  <section class="card card--front" aria-label="Business card front">
    <header class="card__brand-area">
      <span class="brand-square" aria-hidden="true"></span>
      <div class="brand-text">
        <span class="brand-name">TrailStocked.com</span>
        <span class="brand-tagline">Stocked for Trail and Wilderness</span>
      </div>
    </header>

    <div class="card__panel">
      <div class="person">
        <p class="person__name">Daniel Varga</p>
        <p class="person__role">Purchasing Manager</p>
      </div>

      <div class="contact">
        <p class="contact__address">PO BOX 582<br>Ridgefield, IL 60412</p>
        <p class="contact__line">
          <svg viewBox="0 0 13 13" aria-hidden="true"><rect x="3.5" y="2" width="6" height="10.5" rx="1" fill="none" stroke="#fff" stroke-width="1.2"/><rect x="4.8" y="3.5" width="3.4" height="3.5" fill="#fff"/><line x1="4.5" y1="2" x2="4.5" y2="0" stroke="#fff" stroke-width="1"/></svg>
          555 201 4400
        </p>
        <p class="contact__line">
          <svg viewBox="0 0 13 13" aria-hidden="true"><rect x="3" y="1" width="7" height="11.5" fill="#fff"/><g fill="#17497a"><rect x="4.2" y="2.5" width="1.4" height="1.4"/><rect x="7.3" y="2.5" width="1.4" height="1.4"/><rect x="4.2" y="5.3" width="1.4" height="1.4"/><rect x="7.3" y="5.3" width="1.4" height="1.4"/><rect x="5.7" y="9" width="1.6" height="3.5"/></g></svg>
          555 301 7720
        </p>
        <p class="contact__line">
          <svg viewBox="0 0 13 13" aria-hidden="true"><rect x="0.8" y="2.5" width="11.4" height="8" fill="none" stroke="#fff" stroke-width="1.2"/><path d="M1 3l5.5 4.2L12 3" fill="none" stroke="#fff" stroke-width="1.1"/></svg>
          Purchasing@TrailStocked.org
        </p>
        <p class="contact__line">
          <svg viewBox="0 0 13 13" aria-hidden="true"><circle cx="6.5" cy="6.5" r="5.6" fill="none" stroke="#fff" stroke-width="1.1"/><ellipse cx="6.5" cy="6.5" rx="2.4" ry="5.6" fill="none" stroke="#fff" stroke-width="1"/><line x1="1" y1="6.5" x2="12" y2="6.5" stroke="#fff" stroke-width="1"/></svg>
          www.TrailStocked.org
        </p>
      </div>
    </div>

    <svg class="card__stripe" viewBox="0 0 540 32" aria-hidden="true">
      <defs>
        <linearGradient id="stripe-orange-front" x1="0" x2="1"><stop offset="0" stop-color="#f7941d"/><stop offset="1" stop-color="#f15a29"/></linearGradient>
      </defs>
      <rect x="0" y="13" width="540" height="19" fill="#0c2c4d"/>
      <path d="M240 32 L262 13 L280 13 L258 32 Z" fill="#1c5588"/>
      <path d="M254 32 L280 6 Q285 2 292 2 L540 2 L540 32 Z" fill="url(#stripe-orange-front)"/>
    </svg>
  </section>

  <section class="card card--back" aria-label="Business card back">
    <div class="back-brand">
      <span class="brand-square" aria-hidden="true"></span>
      <span class="back-brand__name">TrailStocked</span>
    </div>
    <span class="back-divider" aria-hidden="true"></span>
    <p class="back-tagline">Stocked for<br>Trail and<br>Wilderness</p>

    <svg class="card__stripe" viewBox="0 0 540 32" aria-hidden="true">
      <defs>
        <linearGradient id="stripe-orange-back" x1="0" x2="1"><stop offset="0" stop-color="#f7941d"/><stop offset="1" stop-color="#f15a29"/></linearGradient>
      </defs>
      <rect x="0" y="13" width="540" height="19" fill="#0c2c4d"/>
      <path d="M240 32 L262 13 L280 13 L258 32 Z" fill="#1c5588"/>
      <path d="M254 32 L280 6 Q285 2 292 2 L540 2 L540 32 Z" fill="url(#stripe-orange-back)"/>
    </svg>
  </section>

</main>
</body>
</html>
```